Marcus Fenwold Economic Development, LLC Brochure

Need a concise handout for upcoming conference.

Target Market(s)

Local government officials.

Font styles to use
Serif
Sans Serif

Colors
EB3D1F
EC4F4E
F09395
F8D3D4
FCEDEE

Requirements
Must have
• Logo must be incorporated. Details provided in the uploads. Looking for nice design package.

```html
<!DOCTYPE html>
<html lang="en">
<head>
<meta charset="utf-8">
<title>Marcus Fenwold Economic Development, LLC Brochure</title>
<link href="https://fonts.googleapis.com/css2?family=Roboto:ital,wght@0,400;0,500;0,700;1,400&display=swap" rel="stylesheet">
<style>
:root{
  --red:#d9202c;
  --red-dark:#8e1119;
  --ink:#231f20;
  --text:#3a3a3a;
  --grey:#8a8a8a;
  --line:#9a9a9a;
  --stage:#dcdcdc;
  --white:#ffffff;
}
*{box-sizing:border-box;margin:0;padding:0}
html,body{width:1200px;height:2251px;overflow:hidden}
body{background:var(--stage);font-family:"Roboto",Arial,sans-serif;color:var(--text);position:relative}
.page{position:absolute;width:450px;height:652px;background:var(--white);overflow:hidden}
.page-cover{left:93px;top:67px}
.page-services{left:651px;top:67px}
.page-founder{left:93px;top:791px}
.page-associate{left:651px;top:791px}
.page-clients{left:93px;top:1514px}
.art{position:absolute;left:0;top:0}
.brand{position:absolute;display:flex;align-items:center;gap:9px;color:var(--ink)}
.brand-square{background:var(--red);flex:none}
.brand-name{font-weight:400;line-height:1.15;letter-spacing:.04em;text-transform:uppercase}
.brand-name span{display:block;text-transform:none;letter-spacing:0}
.cover-brand{left:31px;top:40px}
.cover-brand .brand-square{width:42px;height:42px}
.cover-brand .brand-name{font-size:19px}
.cover-brand .brand-name span{font-size:15px;margin-top:3px}
.footer-brand{left:39px;top:605px}
.footer-brand .brand-square{width:22px;height:22px}
.footer-brand .brand-name{font-size:8.5px}
.footer-brand .brand-name span{font-size:6.5px;margin-top:1px}
.cover-url{position:absolute;right:38px;top:611px;color:var(--white);font-size:12.5px;letter-spacing:.01em}
.cover-url-bar{position:absolute;right:0;top:618px;width:23px;height:6px;background:var(--red)}
.firm-title{position:absolute;left:0;width:450px;top:112px;text-align:center;color:var(--white);font-weight:500;font-size:16.5px}
.firm-intro{position:absolute;left:38px;width:374px;top:140px;text-align:center;color:var(--white);font-size:10px;line-height:12.2px}
.services-tag{position:absolute;left:114px;top:285px;width:205px;height:22px;background:var(--grey);color:var(--white);font-weight:500;font-size:15px;text-align:center;line-height:22px}
.service{position:absolute;display:flex;align-items:center;gap:10px;font-size:10px;line-height:12.2px;color:var(--text)}
.service svg{flex:none}
.section-red{color:var(--red);font-weight:700}
.analysis-title{position:absolute;left:0;width:450px;top:466px;text-align:center;font-size:15px}
.arrow-list{position:absolute;list-style:none;font-size:10px;line-height:12.2px}
.arrow-list li{position:relative;padding-left:13px;margin-bottom:7.5px}
.arrow-list li::before{content:"";position:absolute;left:0;top:2px;border-left:7px solid var(--ink);border-top:4px solid transparent;border-bottom:4px solid transparent}
.drop-line{position:absolute;width:1px;background:#555}
.drop-line::after{content:"";position:absolute;left:-2px;bottom:-3px;width:5px;height:5px;border-radius:50%;background:#555}
.kicker{position:absolute;font-size:16px;font-weight:700;color:var(--red)}
.person{position:absolute;font-size:15px;font-weight:400;color:var(--ink)}
.bio{position:absolute;font-size:10px;line-height:12.2px;color:var(--text)}
.bio p{margin-bottom:6px}
.edu-title{position:absolute;font-size:16px;font-weight:700;color:var(--red)}
.edu-list{position:absolute;list-style:none;font-size:9.8px;line-height:12px;font-style:italic}
.edu-list li{position:relative;margin-bottom:6px}
.edu-list li::before{content:"";position:absolute;top:2px;border-left:7px solid var(--ink);border-top:4px solid transparent;border-bottom:4px solid transparent}
.edu-left li{padding-left:13px}
.edu-left li::before{left:0}
.edu-right{text-align:right}
.edu-right li::before{position:static;display:inline-block;margin-right:6px;vertical-align:0}
.edu-list em{color:var(--red)}
.right{text-align:right}
.client-list{position:absolute;list-style:none;font-size:10px;line-height:16.7px;color:var(--text)}
.client-list li{padding-left:7px;position:relative}
.client-list li::before{content:"";position:absolute;left:0;top:7px;width:3px;height:3px;border-radius:50%;background:var(--red)}
.client-list .wrap{line-height:12px;padding-top:2px}
</style>
</head>
<body>

<section class="page page-cover">
  <svg class="art" width="450" height="652" viewBox="0 0 450 652">
    <defs>
      <linearGradient id="towerTone" x1="0" y1="0" x2="1" y2="1">
        <stop offset="0" stop-color="#ffffff"/>
        <stop offset=".25" stop-color="#e8b9b8"/>
        <stop offset=".55" stop-color="#c06c72"/>
        <stop offset="1" stop-color="#4e2434"/>
      </linearGradient>
      <clipPath id="stripeTop"><rect x="0" y="0" width="450" height="260"/></clipPath>
    </defs>
    <polygon points="450,124 81,652 450,652" fill="var(--ink)"/>
    <polygon clip-path="url(#stripeTop)" points="450,106 450,124 81,652 69,652" fill="var(--red)"/>
    <path role="img" aria-label="Photo of a glass tower seen from below" d="M0,160 L186,160 A192,192 0 0 1 186,556 L0,556 Z" fill="url(#towerTone)"/>
  </svg>
  <div class="brand cover-brand">
    <div class="brand-square"></div>
    <div class="brand-name">Marcus Fenwold<span>Economic Development</span></div>
  </div>
  <div class="cover-url">www.mfeconomicdevelopment-llc.com</div>
  <div class="cover-url-bar"></div>
</section>

<section class="page page-services">
  <svg class="art" width="450" height="652" viewBox="0 0 450 652">
    <defs>
      <linearGradient id="skylineRed" x1="0" y1="0" x2="0" y2="1">
        <stop offset="0" stop-color="#b3141f"/>
        <stop offset="1" stop-color="var(--red)"/>
      </linearGradient>
    </defs>
    <path role="img" aria-label="Red-toned photo of a downtown skyline" d="M0,0 H450 V165 C450,232 350,270 225,270 C100,270 0,232 0,165 Z" fill="url(#skylineRed)"/>
    <path d="M81,-45 A144,144 0 0 0 369,-45 L304,-45 A79,79 0 0 1 146,-45 Z" fill="var(--white)"/>
    <line x1="0" y1="644" x2="170" y2="644" stroke="var(--line)" stroke-width="1"/>
    <polyline points="170,644 186,616 450,616" fill="none" stroke="var(--line)" stroke-width="1"/>
    <polygon points="184,633 193,621 450,621 450,633" fill="var(--red)"/>
  </svg>
  <h2 class="firm-title">MFED, LLC QUALIFICATIONS</h2>
  <p class="firm-intro">Marcus Fenwold Economic Development, LLC. is an economic development firm offering a broad range of development expertise to public, private and institutional clients. With strategic guidance, we help navigate public-private partnerships, local government policies, creative incentive financing, project/program management, and many more of the challenges facing our clients. We present an unsurpassed level of quality and commitment by providing sensible solutions that are customized to meet the shifting needs of today’s economy.</p>
  <div class="services-tag">Services Include:</div>

  <div class="service" style="left:37px;top:322px">
    <svg width="28" height="28" viewBox="0 0 28 28"><circle cx="14" cy="14" r="14" fill="var(--grey)"/><path d="M6 15 L11 11 L15 13 L19 10 L22 13 L17 18 L11 18 Z" fill="none" stroke="#fff" stroke-width="1.4" stroke-linejoin="round"/></svg>
    <span>Public Private<br>Partnership Structuring</span>
  </div>
  <div class="service" style="left:37px;top:360px">
    <svg width="28" height="28" viewBox="0 0 28 28"><circle cx="14" cy="14" r="14" fill="var(--grey)"/><path d="M9 20V15M12 20V12M15 20V14M18 20V10" stroke="#fff" stroke-width="2"/></svg>
    <span>Incentive Negotiations</span>
  </div>
  <div class="service" style="left:37px;top:397px">
    <svg width="28" height="28" viewBox="0 0 28 28"><circle cx="14" cy="14" r="14" fill="var(--grey)"/><path d="M8 12 L12 9 L15 11 L20 7" fill="none" stroke="#fff" stroke-width="1.4"/><path d="M10 21V17M13 21V15M16 21V16M19 21V13" stroke="#fff" stroke-width="2"/></svg>
    <span>Creating and Amending<br>Tax Increment<br>Reinvestments Zones</span>
  </div>
  <div class="service" style="left:268px;top:322px">
    <svg width="28" height="28" viewBox="0 0 28 28"><circle cx="14" cy="14" r="14" fill="var(--grey)"/><path d="M9 8 C8 12 13 19 18 20 L20 18 L17 15 L15 16 C13 15 12 13 12 12 L13 10 L10 7 Z" fill="#fff"/></svg>
    <span>Chapter 380 Grant<br>Contract Negotiations</span>
  </div>
  <div class="service" style="left:268px;top:360px">
    <svg width="28" height="28" viewBox="0 0 28 28"><circle cx="14" cy="14" r="14" fill="var(--grey)"/><path d="M7 14 L14 8 L21 14 M9 13 V20 H19 V13" fill="none" stroke="#fff" stroke-width="1.4"/></svg>
    <span>City Council Workshops</span>
  </div>
  <div class="service" style="left:268px;top:397px">
    <svg width="28" height="28" viewBox="0 0 28 28"><circle cx="14" cy="14" r="14" fill="var(--grey)"/><rect x="9" y="7" width="10" height="14" fill="none" stroke="#fff" stroke-width="1.3"/><path d="M11 18V15M14 18V13M17 18V11" stroke="#fff" stroke-width="1.4"/></svg>
    <span>Economic Impact<br>Reporting</span>
  </div>

  <h3 class="analysis-title section-red">Real Estate Financial Analysis including:</h3>
  <ul class="arrow-list" style="left:42px;top:505px">
    <li>Taxable Value Analysis</li>
    <li>Pro-forma Analysis</li>
    <li>Underwriting of<br>Incentive Package</li>
  </ul>
  <ul class="arrow-list" style="left:268px;top:505px">
    <li>Market/Financial Feasibility</li>
    <li>Cost/Benefit Analysis</li>
    <li>Appraisal review</li>
  </ul>

  <div class="brand footer-brand">
    <div class="brand-square"></div>
    <div class="brand-name">Marcus Fenwold<span>Economic Development</span></div>
  </div>
</section>

<section class="page page-founder">
  <svg class="art" width="450" height="652" viewBox="0 0 450 652">
    <defs>
      <linearGradient id="cityRed" x1="0" y1="0" x2="1" y2="1">
        <stop offset="0" stop-color="var(--red)"/>
        <stop offset="1" stop-color="var(--red-dark)"/>
      </linearGradient>
    </defs>
    <circle role="img" aria-label="Red-toned aerial photo of a city" cx="450" cy="652" r="225" fill="url(#cityRed)"/>
    <circle cx="450" cy="652" r="103" fill="var(--white)"/>
    <circle cx="461" cy="652" r="31" fill="var(--red-dark)"/>
    <line x1="0" y1="644" x2="170" y2="644" stroke="var(--line)" stroke-width="1"/>
    <polyline points="170,644 186,616 450,616" fill="none" stroke="var(--line)" stroke-width="1"/>
    <polygon points="184,633 193,621 450,621 450,633" fill="var(--red)"/>
  </svg>
  <div class="drop-line" style="left:42px;top:0;height:100px"></div>
  <h2 class="kicker" style="left:40px;top:116px">MFED QUALIFICATIONS</h2>
  <h3 class="person" style="left:40px;top:148px">Marcus Fenwold</h3>
  <div class="bio" style="left:40px;top:177px;width:380px">
    <p>With over 25 years of experience, Marcus Fenwold oversees economic development and real estate development projects for Marcus Fenwold Economic Development, LLC. Marcus focuses on public-private partnerships for medium to large size real estate projects. His efforts include conducting feasibility analysis, contract negotiations and financing mechanisms such as TIF, abatements, and rebates, for both public and private sector clients. Marcus’s extensive experience with multifaceted complex projects provides him with unique insight and creative solutions for complex problems.</p>
    <p>His previous projects include the successful development and redevelopment of The Spire, Northgate, Meridian Plaza and West Row in Glenwick, restructuring Harbor Park in Ashcombe, Lakeside Crossing in Bellmere, and Bayfront Mall in Port Kestrel. Additionally, he has both managed and created multiple tax increment reinvestment zones and public improvement districts addressing a wide range of issues throughout the region.</p>
  </div>
  <h3 class="edu-title" style="left:40px;top:398px">Education:</h3>
  <ul class="edu-list edu-left" style="left:40px;top:425px">
    <li><em>Master of Public Administration</em> - North Plains University.</li>
    <li><em>Bachelor of Arts – Political Science</em> – High Plains Tech University</li>
  </ul>
  <div class="brand footer-brand">
    <div class="brand-square"></div>
    <div class="brand-name">Marcus Fenwold<span>Economic Development</span></div>
  </div>
</section>

<section class="page page-associate">
  <svg class="art" width="450" height="652" viewBox="0 0 450 652">
    <defs>
      <linearGradient id="campusRed" x1="0" y1="0" x2="1" y2="1">
        <stop offset="0" stop-color="#b51a24"/>
        <stop offset="1" stop-color="#5e1015"/>
      </linearGradient>
    </defs>
    <ellipse role="img" aria-label="Red-toned photo of a campus clock tower and fountain" cx="0" cy="0" rx="252" ry="233" fill="url(#campusRed)"/>
    <circle cx="52" cy="0" r="105" fill="var(--white)"/>
    <circle cx="52" cy="0" r="52" fill="#6b1a1f"/>
    <line x1="0" y1="644" x2="170" y2="644" stroke="var(--line)" stroke-width="1"/>
    <polyline points="170,644 186,616 450,616" fill="none" stroke="var(--line)" stroke-width="1"/>
    <polygon points="184,633 193,621 450,621 450,633" fill="var(--red)"/>
  </svg>
  <div class="drop-line" style="left:394px;top:0;height:200px"></div>
  <h2 class="kicker right" style="right:55px;top:214px">MFED QUALIFICATIONS</h2>
  <h3 class="person right" style="right:55px;top:248px">Clara Whitby</h3>
  <div class="bio right" style="right:55px;top:274px;width:350px">
    <p>Clara focuses on economic development and real estate development projects and maximizing opportunities for public-private partnerships. Clara is a former Business Development Coordinator for the City of Glenwick’s Economic Development Department. During her time with the City, her responsibilities included the implementation of incentives, including tax abatements, economic development program grants, tax increment financing, EB-5 funding, and state tax incentives.</p>
    <p>Prior to joining the City of Glenwick, Clara was an Analyst with Keystone Valuation Resources in Glenwick, where her work focused on commercial real estate appraisals used for loan underwriting purposes for a variety of property types, including office, hotel, industrial, retail, and multifamily. Earlier in her career, Clara was an Associate in Crestmark Realty’s brokerage services division. In her role, she was responsible for negotiating and executing office and industrial lease and sale transactions.</p>
  </div>
  <h3 class="edu-title right" style="right:55px;top:480px">Education:</h3>
  <ul class="edu-list edu-right" style="right:55px;top:509px;width:300px">
    <li><em>Master of Business Administration</em> – Corporate Finance – Trinity River Christian University</li>
    <li><em>BBA – Management</em> – Brazos State University</li>
  </ul>
  <div class="brand footer-brand">
    <div class="brand-square"></div>
    <div class="brand-name">Marcus Fenwold<span>Economic Development</span></div>
  </div>
</section>

<section class="page page-clients">
  <svg class="art" width="450" height="652" viewBox="0 0 450 652">
    <defs>
      <linearGradient id="downtownRed" x1="0" y1="0" x2="0" y2="1">
        <stop offset="0" stop-color="var(--red)"/>
        <stop offset=".6" stop-color="#8e1119"/>
        <stop offset="1" stop-color="#3a1a1d"/>
      </linearGradient>
    </defs>
    <ellipse role="img" aria-label="Red-toned photo of downtown towers" cx="0" cy="306" rx="154" ry="262" fill="url(#downtownRed)"/>
    <ellipse cx="0" cy="306" rx="77" ry="162" fill="var(--white)"/>
    <ellipse cx="0" cy="306" rx="39" ry="92" fill="#9c1720"/>
    <line x1="0" y1="644" x2="170" y2="644" stroke="var(--line)" stroke-width="1"/>
    <polyline points="170,644 186,616 450,616" fill="none" stroke="var(--line)" stroke-width="1"/>
    <polygon points="184,633 193,621 450,621 450,633" fill="var(--red)"/>
  </svg>
  <div class="drop-line" style="left:173px;top:0;height:121px"></div>
  <h2 class="kicker" style="left:177px;top:139px">Public Clients:</h2>
  <ul class="client-list" style="left:179px;top:166px">
    <li>Alder Springs</li><li>Ashcombe</li><li>Bellmere</li><li>Briar Hollow</li><li>Caddo Ridge</li><li>Cedar Fen</li><li>Colby Mills</li><li>Crestwater</li><li>Dunmore</li>
  </ul>
  <ul class="client-list" style="left:314px;top:166px">
    <li>Elm Reach</li><li>Glenwick</li><li>Fairhaven</li><li>Greyford</li><li>Hollis Bend</li><li>Kestrel</li><li>Lark Hill</li><li>Millbrook</li><li>Stonebridge</li>
  </ul>
  <h2 class="kicker" style="left:175px;top:358px">Private Clients:</h2>
  <ul class="client-list" style="left:179px;top:384px">
    <li>Ashford Homes</li><li>Centralis American</li><li>Bicentra Real Estate</li><li>Juniper Equities</li><li>Fairline Diversified</li><li>Developments</li><li>Halden</li><li>Quorra Global</li><li>Jasper Shaw</li>
  </ul>
  <ul class="client-list" style="left:314px;top:384px">
    <li>Kelvo Realty</li><li>Regalis Realty</li><li>Meridel Homes</li><li>NK Developments</li><li>RQL</li><li>Rex Galloway</li><li>Tamber Outlets</li><li>Tradecrest</li><li class="wrap">Unity Commercial<br>Development</li>
  </ul>
  <div class="brand footer-brand">
    <div class="brand-square"></div>
    <div class="brand-name">Marcus Fenwold<span>Economic Development</span></div>
  </div>
</section>

</body>
</html>
```